Business Card Design

Just looking for a good designs that looks good with our company logo. I'd like it to be simple and to the point. Just including contact information, our logo, and my name somewhere on the card so future clients know who they're contacting, and a couple services offered. The two images I attached are pictures of our logo. I don't care which color they they are, I just attached both images to give a reference of logo colors depending on the color of the card.
Names: Calvin Prewitt
Phone: 555-247-9061
Email: tidyturfcrew@mailvista.net
Services offered:
Mowing
Fertilization
Aeration
Bed & tree maintenance
and more.
Industry/Entity Type
Business
Contact Information for Business Card
Names: Calvin Prewitt
Phone: 555-247-9061
Look and feel

```html
<!DOCTYPE html>
<html lang="en">
<head>
<meta charset="utf-8">
<title>Tidy Turf Crew – Business Card</title>
<link href="https://fonts.googleapis.com/css2?family=Open+Sans:wght@400;600;700&display=swap" rel="stylesheet">
<style>
  :root {
    --backdrop: #d8d3cd;
    --card: #eef0ef;
    --ink: #2c2f34;
    --ink-soft: #3d4046;
    --red: #d8423a;
    --red-light: #e2675e;
    --charcoal: #3a3d43;
    --white: #ffffff;
  }
  * { margin: 0; padding: 0; box-sizing: border-box; }
  html, body {
    width: 1200px; height: 969px; overflow: hidden;
    background: var(--backdrop);
    font-family: "Open Sans", Arial, sans-serif;
  }
  .card {
    position: absolute; left: 80px; top: 204px;
    width: 1040px; height: 560px;
    background: var(--card);
    border-radius: 14px;
    overflow: hidden;
    box-shadow: 0 18px 40px rgba(0,0,0,.18);
  }
  .brand {
    position: absolute; left: 60px; top: 160px; width: 390px;
    display: flex; align-items: center; gap: 18px;
  }
  .brand-dot {
    width: 54px; height: 54px; border-radius: 50%;
    background: var(--red); flex: none;
  }
  .brand-name {
    font-weight: 700; font-size: 44px; line-height: 1.05;
    color: var(--charcoal);
  }
  .owner {
    position: absolute; left: 534px; top: 50px;
    font-size: 54px; font-weight: 600; color: var(--ink);
  }
  .services {
    position: absolute; left: 534px; top: 152px;
    list-style: none; color: var(--ink-soft);
    font-size: 30px; line-height: 55px;
  }
  .services li::before { content: "- "; }
  .contact-band {
    position: absolute; left: 0; top: 420px; width: 100%; height: 80px;
    background: var(--red);
    display: flex; align-items: center;
    padding: 0 48px;
    color: var(--white); font-size: 28px;
  }
  .email { flex: 1; }
  .icon {
    width: 52px; height: 52px; flex: none;
  }
  .icon-mail { margin-right: 64px; }
  .icon-phone { margin-right: 22px; }
  .phone { font-size: 30px; margin-right: 40px; }
  .accent-strip {
    position: absolute; left: 0; top: 500px; width: 100%; height: 30px;
    display: flex;
  }
  .accent-strip span { height: 100%; }
  .seg-light { width: 18%; background: var(--red-light); }
  .seg-dark { width: 26%; background: var(--charcoal); }
  .seg-red { width: 28%; background: var(--red); }
  .seg-end { width: 28%; background: var(--charcoal); }
</style>
</head>
<body>
  <main class="card">
    <div class="brand">
      <span class="brand-dot"></span>
      <span class="brand-name">Tidy Turf Crew</span>
    </div>

    <h1 class="owner">Calvin Prewitt</h1>

    <ul class="services">
      <li>Mowing</li>
      <li>Fertilization</li>
      <li>Aeration</li>
      <li>Bed &amp; tree maintenance</li>
    </ul>

    <div class="contact-band">
      <span class="email">tidyturfcrew@mailvista.net</span>
      <svg class="icon icon-mail" viewBox="0 0 52 52" aria-hidden="true">
        <circle cx="26" cy="26" r="23" fill="none" stroke="#3a3d43" stroke-width="3"/>
        <rect x="14" y="17" width="24" height="18" rx="2" fill="none" stroke="#3a3d43" stroke-width="3"/>
        <path d="M14 19 L26 28 L38 19" fill="none" stroke="#3a3d43" stroke-width="3"/>
      </svg>
      <svg class="icon icon-phone" viewBox="0 0 52 52" aria-hidden="true">
        <circle cx="26" cy="26" r="23" fill="none" stroke="#3a3d43" stroke-width="3"/>
        <rect x="18" y="12" width="16" height="28" rx="3" fill="none" stroke="#3a3d43" stroke-width="3"/>
        <line x1="22" y1="34" x2="30" y2="34" stroke="#3a3d43" stroke-width="3"/>
      </svg>
      <span class="phone">555-247-9061</span>
    </div>

    <div class="accent-strip">
      <span class="seg-light"></span>
      <span class="seg-dark"></span>
      <span class="seg-red"></span>
      <span class="seg-end"></span>
    </div>
  </main>
</body>
</html>
```